Law Firm Needs Brochure Redesign Using New Logo

We are a personal injury law firm that does auto injuries and other personal injury cases. We want a new brochure that has our updated logo and information. Instead of gold and black, we want more navy, as matches the new logo. The Auto Liability portion should read: "(required by the state of Arizona in the amounts of $25,000 per person / $50,000 per accident, but a higher amount may be best )." The other information can remain the same. We'd like the brochure to keep the same professional tone as the previous brochure.
Our website is https://www.brandtlegalpartners.example/.

```html
<!DOCTYPE html>
<html lang="en">
<head>
<meta charset="utf-8">
<title>Brandt Legal Partners – Car Accident Brochure</title>
<link rel="stylesheet" href="https://fonts.googleapis.com/css2?family=Inter:wght@400;600;700&family=Montserrat:wght@700;800&family=Ubuntu:wght@500&display=swap">
<style>
:root{
  --navy:#13254a;
  --navy-deep:#0f1d3b;
  --ink:#1d1f26;
  --steel:#3b6198;
  --slate:#6f7488;
  --paper:#f4f4f4;
  --page:#ebebeb;
  --text:#1f2228;
  --muted:#4a4e57;
  --white:#ffffff;
}
*{margin:0;padding:0;box-sizing:border-box}
html,body{width:1200px;height:900px;overflow:hidden;background:var(--page);font-family:"Inter",Arial,sans-serif;color:var(--text)}
.sheet{position:absolute;left:225px;width:750px;height:425px;display:flex;box-shadow:0 6px 18px rgba(0,0,0,.18)}
.sheet--outside{top:15px}
.sheet--inside{top:460px}
.panel{position:relative;width:250px;height:425px;overflow:hidden}
.panel-bg{position:absolute;inset:0;width:100%;height:100%}
.brand{position:absolute;display:flex;align-items:center;gap:5px;font-family:"Inter",Arial,sans-serif;font-weight:700;font-size:9px;letter-spacing:.08em;text-transform:uppercase}
.brand-dot{width:9px;height:9px;border-radius:50%;background:currentColor;display:block}
.brand--light{color:var(--white)}
.brand--navy{color:var(--navy)}

/* stats flap */
.stats-box{position:absolute;left:14px;top:14px;width:222px;height:396px;background:var(--navy);border:1.5px solid var(--steel);color:var(--white);text-align:center}
.stat-icon{position:absolute;left:50%;transform:translateX(-50%);width:30px;height:30px;border-radius:50%;background:var(--white)}
.stat-figure{position:absolute;left:0;right:0;font-size:17px;font-weight:600}
.stat-note{position:absolute;left:20px;right:20px;font-size:7px;line-height:1.35;color:#8fa6cc}
.stats-promise{position:absolute;left:14px;right:14px;bottom:16px;font-size:6.6px;line-height:1.4}

/* back panel */
.practice-note{position:absolute;left:40px;right:20px;top:118px;font-size:6.6px;line-height:1.35;color:var(--white);text-align:center}
.contact{position:absolute;left:30px;top:318px;color:var(--white);font-size:6.6px;line-height:1.3}
.contact-list{list-style:none;margin-top:14px}
.contact-list li{display:flex;gap:6px;align-items:flex-start;margin-bottom:7px}
.contact-list svg{flex:none;margin-top:1px}
.contact-link{color:#8fb0e0}

/* cover */
.cover-title{position:absolute;left:20px;top:50px;font-family:"Ubuntu",sans-serif;font-weight:500;font-size:27px;line-height:1.0;color:var(--white)}
.cover-title .highlight{display:inline-block;background:var(--navy);padding:0 5px 2px;margin-left:-4px}
.cover-tagline{position:absolute;left:20px;top:176px;width:150px;font-size:8px;line-height:1.3;color:var(--white)}

/* tips */
.tips-title{position:absolute;left:16px;top:10px;width:218px;height:44px;background:var(--navy);color:var(--white);font-family:"Montserrat",sans-serif;font-weight:700;font-size:10px;line-height:1.15;text-align:center;text-transform:uppercase;padding:9px 20px 0}
.tips-list{position:absolute;left:0;top:106px;right:14px;list-style:none}
.tips-list li{position:relative;padding-left:14px;font-size:6.1px;line-height:1.3;margin-bottom:8.5px;color:var(--muted)}
.tips-list li::before{content:"";position:absolute;left:0;top:0;border-left:6px solid var(--navy);border-top:6px solid transparent;border-bottom:6px solid transparent}
.tips-list strong{color:var(--text);font-weight:700}

/* coverage */
.coverage-head{position:absolute;left:8px;top:10px;right:50px}
.coverage-head h2{font-size:8.2px;font-weight:700;color:var(--navy);text-transform:uppercase;margin-bottom:5px}
.coverage-head p{font-size:6.6px;line-height:1.3;color:var(--text)}
.coverage-list{position:absolute;left:10px;right:12px;top:200px;list-style:none}
.coverage-list li{position:relative;padding-left:14px;margin-bottom:13px}
.coverage-list li::before{content:"›";position:absolute;left:0;top:-3px;font-size:11px;color:var(--text)}
.coverage-list h3{font-size:8px;font-weight:600;color:var(--navy);margin-bottom:3px;line-height:1.15}
.coverage-list p{font-size:6px;line-height:1.3;color:var(--muted)}

/* safe behavior */
.safe-title{position:absolute;left:14px;top:98px;font-family:"Montserrat",sans-serif;font-weight:800;font-size:17px;line-height:1.05;color:var(--white);text-transform:uppercase}
.safe-list{position:absolute;left:18px;right:24px;top:192px;list-style:none}
.safe-list li{margin-bottom:18px}
.safe-list h3{font-size:8.4px;font-weight:700;color:var(--text);margin-bottom:3px}
.safe-list p{font-size:6.4px;line-height:1.3;color:var(--muted)}
.safe-list .aside{margin-top:4px;font-weight:700;color:var(--text);font-size:5.8px}
</style>
</head>
<body>

<section class="sheet sheet--outside" aria-label="Brochure outside">

  <article class="panel panel--stats" style="background:var(--ink)">
    <div class="stats-box">
      <span class="stat-icon" style="top:32px">
        <svg width="30" height="30" viewBox="0 0 30 30"><rect x="8" y="13" width="14" height="6" rx="2" fill="#2e9c7d"/><path d="M10 13l2-4h6l2 4z" fill="#2e9c7d"/><circle cx="11" cy="20" r="1.6" fill="#333"/><circle cx="19" cy="20" r="1.6" fill="#333"/></svg>
      </span>
      <p class="stat-figure" style="top:78px">107,000+</p>
      <p class="stat-note" style="top:103px">crashes will happen in the state of Arizona this year.</p>
      <span class="stat-icon" style="top:150px">
        <svg width="30" height="30" viewBox="0 0 30 30"><path d="M10 20v-5a5 5 0 0 1 10 0v5z" fill="#e0424a"/><rect x="8" y="20" width="14" height="2.5" fill="#555"/></svg>
      </span>
      <p class="stat-figure" style="top:196px">700+</p>
      <p class="stat-note" style="top:221px">among them will result in fatalities.</p>
      <p class="stats-promise">If we don't win, you don't pay attorney fees. That seems fair to us. Know what's happening with your case, get the answers to your questions and work on getting better with the confidence that you've got an excellent group of people working for you.</p>
    </div>
  </article>

  <article class="panel panel--back">
    <svg class="panel-bg" viewBox="0 0 250 425" preserveAspectRatio="none">
      <defs><linearGradient id="backPhoto" x1="0" y1="0" x2="1" y2="1"><stop offset="0" stop-color="#5f6378"/><stop offset="1" stop-color="#8c90a3"/></linearGradient></defs>
      <rect width="250" height="425" fill="url(#backPhoto)" role="img" aria-label="Muted photo of a damaged car headlight"/>
      <polygon points="0,170 250,415 250,425 0,425" fill="var(--ink)"/>
      <polygon points="0,150 14,150 250,385 250,400" fill="var(--steel)"/>
      <polygon points="0,180 0,195 160,355 175,355" fill="var(--navy)"/>
      <polygon points="60,205 80,205 170,300 150,300" fill="var(--steel)"/>
    </svg>
    <p class="practice-note">Our primary practice is helping injury victims and their families through the process of insurance claims and litigation related to car accidents, trucking accidents, wrongful death and other serious injuries.</p>
    <div class="contact">
      <span class="brand brand--light" style="position:static"><span class="brand-dot"></span>Brandt Legal</span>
      <ul class="contact-list">
        <li><svg width="7" height="8" viewBox="0 0 10 12"><path d="M5 0a4 4 0 0 1 4 4c0 3-4 8-4 8S1 7 1 4a4 4 0 0 1 4-4z" fill="#fff"/><circle cx="5" cy="4" r="1.5" fill="var(--ink)"/></svg><span>4410 N. Canyon Ridge Road Suite 300<br>Phoenix AZ 85016</span></li>
        <li><svg width="7" height="7" viewBox="0 0 10 10"><path d="M2 0l2 2-1 2c1 1.5 2 2.5 3 3l2-1 2 2-1 2C4 10 0 6 0 2z" fill="#fff"/></svg><span>602.555.0147</span></li>
        <li><svg width="8" height="6" viewBox="0 0 12 8"><rect width="12" height="8" fill="#fff"/><path d="M0 0l6 5 6-5" stroke="var(--ink)" fill="none"/></svg><span class="contact-link">info@brandtlegalpartners.example</span></li>
        <li><svg width="7" height="7" viewBox="0 0 10 10"><circle cx="5" cy="5" r="4.3" stroke="#fff" fill="none"/><path d="M1 5h8M5 1v8" stroke="#fff"/></svg><span class="contact-link">www.brandtlegalpartners.example</span></li>
      </ul>
    </div>
  </article>

  <article class="panel panel--cover">
    <svg class="panel-bg" viewBox="0 0 250 425" preserveAspectRatio="none">
      <defs><linearGradient id="coverPhoto" x1="0" y1="0" x2="1" y2="1"><stop offset="0" stop-color="#6a6f84"/><stop offset=".6" stop-color="#7f8396"/><stop offset="1" stop-color="#9a9eac"/></linearGradient></defs>
      <rect width="250" height="425" fill="url(#coverPhoto)" role="img" aria-label="Photo of a crashed car's front headlight"/>
      <polygon points="250,225 250,425 20,425" fill="var(--paper)"/>
      <polygon points="250,205 250,225 20,425 5,425" fill="var(--steel)"/>
      <polygon points="250,240 250,265 170,325 170,305" fill="var(--navy)"/>
      <polygon points="18,0 55,0 20,35 18,35 0,52 0,38" fill="var(--steel)"/>
      <polygon points="70,0 85,0 45,45 30,45" fill="var(--navy)"/>
      <polygon points="0,395 0,410 15,425 0,425" fill="var(--navy)"/>
    </svg>
    <h1 class="cover-title">Protect<br>your family<br>in case of a<br><span class="highlight">car accident</span></h1>
    <p class="cover-tagline">A little knowledge and preparation go a long way</p>
    <span class="brand brand--navy" style="right:16px;bottom:22px"><span class="brand-dot"></span>Brandt Legal</span>
  </article>
</section>

<section class="sheet sheet--inside" aria-label="Brochure inside">

  <article class="panel panel--tips">
    <svg class="panel-bg" viewBox="0 0 250 425" preserveAspectRatio="none">
      <defs><linearGradient id="tipsPaper" x1="0" y1="0" x2="1" y2="0"><stop offset="0" stop-color="#dcdcdc"/><stop offset="1" stop-color="#f1f1f1"/></linearGradient></defs>
      <rect width="250" height="425" fill="url(#tipsPaper)"/>
      <polygon points="0,0 250,0 250,84 0,34" fill="var(--ink)"/>
      <polygon points="0,34 250,84 250,96 0,46" fill="var(--navy)"/>
      <polygon points="0,22 60,34 0,34" fill="var(--steel)" opacity=".6"/>
    </svg>
    <h2 class="tips-title">Top 10 Tips to Avoid a Crash</h2>
    <ol class="tips-list">
      <li><strong>Anyone making a left turn must wait for all oncoming traffic to clear before proceeding.</strong> Yes, even if the light has turned yellow. Wait to be sure that all traffic has stopped.</li>
      <li><strong>When your light turns green,</strong> check to be sure that no vehicles are entering the intersection late.</li>
      <li><strong>Allow plenty of room between you and the car in front of you.</strong> Traffic can stop in an instant, even if you can't see anything ahead.</li>
      <li><strong>Avoid being distracted.</strong> Teenagers are especially susceptible to losing focus if there are too many friends in the car.</li>
      <li><strong>Keep the volume of your radio down and never wear headphones.</strong> Cars are very soundproof these days, but you need to be able to hear an ambulance or police siren.</li>
      <li><strong>Be especially careful on the weekends and early morning hours.</strong></li>
      <li><strong>Dont speed.</strong> Speed is a factor in most crashes. Street lights are timed and the freeway has traffic. It's likely you won't get there much faster even if you do speed.</li>
      <li><strong>Don't drink and drive.</strong> Many cab companies offer a free service to get you home safe.</li>
      <li><strong>Use your turn signals.</strong> This gives an early warning to vehicles you may not be able to see.</li>
    </ol>
  </article>

  <article class="panel panel--coverage">
    <svg class="panel-bg" viewBox="0 0 250 425" preserveAspectRatio="none">
      <defs>
        <linearGradient id="coveragePaper" x1="0" y1="0" x2="1" y2="0"><stop offset="0" stop-color="#f3f3f3"/><stop offset="1" stop-color="#e4e4e4"/></linearGradient>
        <linearGradient id="roadsidePhoto" x1="0" y1="0" x2="0" y2="1"><stop offset="0" stop-color="#eef0f2"/><stop offset=".45" stop-color="#c9ccc8"/><stop offset="1" stop-color="#8a8462"/></linearGradient>
      </defs>
      <rect width="250" height="425" fill="url(#coveragePaper)"/>
      <polygon points="0,0 250,0 250,130 125,170 0,130" fill="url(#roadsidePhoto)" role="img" aria-label="Photo of a woman in a sun hat beside a car overlooking hills"/>
      <polygon points="0,120 40,130 40,140 0,130" fill="var(--navy)"/>
      <polygon points="250,130 210,145 210,135 250,120" fill="var(--navy)"/>
      <rect x="111" y="152" width="28" height="28" transform="rotate(45 125 166)" fill="var(--navy)"/>
      <path d="M125 157v16M120 168l5 5 5-5" stroke="#fff" stroke-width="1.2" fill="none"/>
    </svg>
    <div class="coverage-head">
      <h2>Have the Right Coverage</h2>
      <p>Many people don't know about the different kinds of insurance available. In addition to health insurance, we suggest:</p>
    </div>
    <ul class="coverage-list">
      <li><h3>Auto Liability</h3><p>(required by the state of Arizona in the amounts of $25,000 per person / $50,000 per accident, but a higher amount may be best).</p></li>
      <li><h3>Uninsured or Underinsured Motorist Coverage</h3><p>This protects YOU when the other driver doesn't have insurance or not enough.</p></li>
      <li><h3>Medical Payments Coverage</h3><p>Up to $5,000 in coverage will be paid out to you no matter who is at fault in an accident and does not need to be reimbursed.</p></li>
      <li><h3>Homeowners / Renters Insurance</h3><p>Protects you in case of injuries on your property as well as damage to your home from covered events.</p></li>
    </ul>
  </article>

  <article class="panel panel--safe">
    <svg class="panel-bg" viewBox="0 0 250 425" preserveAspectRatio="none">
      <defs><linearGradient id="seatbeltPhoto" x1="0" y1="0" x2="1" y2="1"><stop offset="0" stop-color="#3f5680"/><stop offset=".55" stop-color="#2a3550"/><stop offset="1" stop-color="#1a2545"/></linearGradient></defs>
      <rect width="250" height="425" fill="var(--white)"/>
      <polygon points="0,0 250,0 250,40 0,40" fill="var(--ink)"/>
      <polygon points="12,12 240,5 240,140 12,185" fill="url(#seatbeltPhoto)" role="img" aria-label="Photo of a passenger fastening a seatbelt"/>
      <polygon points="240,25 250,25 250,45 240,50" fill="var(--steel)"/>
      <polygon points="18,425 18,355 228,305 228,425" fill="var(--navy)"/>
      <polygon points="95,335 250,295 250,310 95,350" fill="var(--steel)"/>
      <polygon points="145,335 250,308 250,321 145,346" fill="var(--ink)"/>
    </svg>
    <h2 class="safe-title">Model<br>Safe Behavior</h2>
    <ul class="safe-list">
      <li><h3>Always buckle up.</h3><p>Always put your children in car seats/boosters that are rated for their height and weight.</p></li>
      <li><h3>Never Text While Driving.</h3><p>Studies have shown that texting while driving is as dangerous as driving intoxicated.</p><p class="aside">Show your children that no text is more important than your safety. It can wait.</p></li>
    </ul>
    <span class="brand brand--light" style="right:26px;bottom:20px"><span class="brand-dot"></span>Brandt Legal</span>
  </article>
</section>

</body>
</html>
```